International Biotech Startup needs a professionally looking web Design

We need a web design for a small biotech company based in Singapore which has global Pharma and Biotech Customers.

Our current website: www.zelvintralabs.com

However this was generated by few of us. We would require a professional design for biotech companies like us. The appearance of the website should be appealing to users and this is mainly a promotional website without any financial transactions.
Once the design is approved, we will provide the updated text.

Target Market(s)

Pharmaceutical, Biotech, healthcare

Industry/Entity Type

Biotechnology

Coding

Coded - Design and coding required

Number of Pages Required

5+ page

Requirements
Must have
• the website needs favicon.
Nice to have
• Please some of the companies websites that we like the most or they are in the similar domain. We would like to have something like that:
• http://www.pinecrestgenomics.com/
• http://www.marlowtherapeutics.com/
• http://www.tendrix.com/
• http://www.velunar.com/
• www.dornavil.com

```html
<!DOCTYPE html>
<html lang="en">
<head>
<meta charset="utf-8">
<title>About – Zelvintra Labs</title>
<link href="https://fonts.googleapis.com/css2?family=Open+Sans:wght@300;400;600;700;800&display=swap" rel="stylesheet">
<style>
  :root{
    --brand-blue:#2e5590;
    --icon-blue:#7f9bc3;
    --panel-grey:#e8e8e8;
    --ink:#222222;
    --body-grey:#777777;
    --white:#ffffff;
    --photo-light:#dfe6f2;
    --photo-mid:#9fb3d6;
    --photo-green:#8fc27a;
  }
  *{box-sizing:border-box;margin:0;padding:0}
  html,body{width:1200px;height:758px;overflow:hidden;background:var(--white)}
  body{font-family:"Open Sans",Arial,sans-serif;position:relative;color:var(--ink)}

  .sidebar{position:absolute;left:0;top:0;width:116px;height:758px;background:var(--white)}
  .brand-tile{position:absolute;left:2px;top:30px;width:135px;height:137px;background:var(--white);
    box-shadow:1px 2px 4px rgba(0,0,0,.25);z-index:2;display:flex;flex-direction:column;align-items:center;justify-content:center;gap:8px}
  .brand-dot{width:56px;height:56px;border-radius:50%;background:var(--brand-blue)}
  .brand-name{font-size:16px;font-weight:700;color:var(--brand-blue)}

  .nav{position:absolute;left:0;top:192px;width:124px;list-style:none}
  .nav-item{position:absolute;left:0;width:124px;text-align:center}
  .nav-icon{display:block;margin:0 auto}
  .nav-label{display:block;font-size:13px;color:var(--ink);margin-top:6px;letter-spacing:.2px}

  .about-panel{position:absolute;left:116px;top:0;width:479px;height:758px;background:var(--panel-grey)}
  .about-title{position:absolute;left:87px;top:118px;font-size:38px;font-weight:700;letter-spacing:.5px}
  .about-lead{position:absolute;left:89px;top:236px;width:260px;font-size:17.5px;line-height:22px;font-weight:600;color:var(--brand-blue)}
  .about-body{position:absolute;left:90px;top:330px;width:350px;font-size:13px;line-height:22px;font-weight:400;color:var(--body-grey)}
  .video-link{position:absolute;left:88px;top:613px;font-size:13px;font-weight:700;letter-spacing:.2px;color:var(--ink);text-decoration:none}
  .video-link::after{content:"";display:inline-block;margin-left:7px;border-left:8px solid var(--ink);border-top:5px solid transparent;border-bottom:5px solid transparent}

  .top-brand{position:absolute;left:1050px;top:32px;display:flex;align-items:center;gap:6px}
  .top-brand-name{font-size:17px;font-weight:700;color:var(--brand-blue)}
  .top-brand-dot{width:10px;height:10px;border-radius:50%;background:#999}

  .lab-photo{position:absolute;left:595px;top:130px;width:551px;height:431px;
    background:
      radial-gradient(ellipse at 30% 25%,rgba(143,194,122,.75),transparent 45%),
      radial-gradient(ellipse at 85% 20%,rgba(143,194,122,.55),transparent 40%),
      linear-gradient(180deg,var(--photo-light),var(--photo-mid) 60%,#c8d3e8)}
  .video-caption{position:absolute;left:595px;top:611px;width:551px;text-align:center;font-size:16px;font-weight:600;color:#111}
</style>
</head>
<body>
  <aside class="sidebar">
    <div class="brand-tile">
      <span class="brand-dot"></span>
      <span class="brand-name">Zelvintra</span>
    </div>
    <ul class="nav">
      <li class="nav-item" style="top:2px">
        <svg class="nav-icon" width="70" height="70" viewBox="0 0 70 70" aria-hidden="true">
          <circle cx="35" cy="35" r="34" fill="var(--icon-blue)"/>
          <g fill="none" stroke="#fff" stroke-width="3" stroke-linecap="round">
            <path d="M30 18 L40 34"/><path d="M26 52 H48"/><path d="M38 52 a10 10 0 0 0 4-16"/><path d="M24 42 H36"/>
          </g>
        </svg>
        <span class="nav-label">TECHNOLOGY</span>
      </li>
      <li class="nav-item" style="top:120px">
        <svg class="nav-icon" width="70" height="70" viewBox="0 0 70 70" aria-hidden="true">
          <circle cx="35" cy="35" r="34" fill="var(--icon-blue)"/>
          <path d="M29 14 H41 M31 14 V30 a14 14 0 1 0 8 0 V14" fill="none" stroke="#fff" stroke-width="3"/>
          <circle cx="35" cy="43" r="9" fill="#fff"/>
        </svg>
        <span class="nav-label">PRODUCTS</span>
      </li>
      <li class="nav-item" style="top:241px">
        <svg class="nav-icon" width="70" height="70" viewBox="0 0 70 70" aria-hidden="true">
          <circle cx="35" cy="35" r="34" fill="var(--icon-blue)"/>
          <rect x="24" y="16" width="24" height="32" fill="#fff"/>
          <g stroke="var(--icon-blue)" stroke-width="2"><path d="M28 23 H44 M28 28 H44 M28 33 H44 M28 38 H38"/></g>
        </svg>
        <span class="nav-label">NEWS</span>
      </li>
      <li class="nav-item" style="top:356px">
        <svg class="nav-icon" width="70" height="70" viewBox="0 0 70 70" aria-hidden="true">
          <circle cx="35" cy="35" r="34" fill="var(--icon-blue)"/>
          <g fill="#fff">
            <circle cx="24" cy="24" r="5"/><path d="M15 40 a9 9 0 0 1 18 0 Z"/>
            <circle cx="46" cy="36" r="5"/><path d="M37 52 a9 9 0 0 1 18 0 Z"/>
          </g>
        </svg>
        <span class="nav-label">CONTACT</span>
      </li>
    </ul>
  </aside>

  <main class="about-panel">
    <h1 class="about-title">ABOUT</h1>
    <h2 class="about-lead">Zelvintra Labs is a biotech startup, with its main office and R&amp;D lab in Singapore</h2>
    <p class="about-body">Our company uses the artificial cell membrane (ACM) platform to produce tailor-made products and programs centered around 'hard targets' in drug discovery. Typically, these are membrane protein targets that cannot be reliably produced using cell-lines. The mission of Zelvintra Labs is to de-risk early stage drug discovery by significantly lowering the costs and time required for drug and antibody screening.</p>
    <a class="video-link" href="#videos">SEE THE VIDEOS</a>
  </main>

  <div class="top-brand">
    <span class="top-brand-name">Zelvintra Labs</span>
    <span class="top-brand-dot"></span>
  </div>

  <div class="lab-photo" role="img" aria-label="Laboratory scene with a microscope, glass flasks and green plant seedlings"></div>
  <p class="video-caption">Video description of ACMs (Clipwave)</p>
</body>
</html>
```